iOS splash screen for fitness app

Hi there I would like a splash screen designed for an iOS app for training as well as the icon for it.

Splash screen: 750 x 1334 pixels
Icon: 1024 x 1024 pixels

The app is an interval training app for training on stairs. I would like the icon and splash screen related to running up and down stairs.

```html
<!DOCTYPE html>
<html lang="en">
<head>
<meta charset="UTF-8">
<title>Stair Interval Training – Splash Screen</title>
<style>
  :root {
    --backdrop: #e6e6e6;
    --coral: #f7666f;
    --pink: #f55d95;
    --pink-light: #f9a6c9;
    --pink-pale: #fcd3e3;
    --white: #ffffff;
    --spinner: #ef4f74;
  }
  * { margin: 0; padding: 0; box-sizing: border-box; }
  html, body {
    width: 1200px;
    height: 600px;
    overflow: hidden;
    background: var(--backdrop);
  }
  .canvas {
    position: relative;
    width: 1200px;
    height: 600px;
  }
  .splash-screen {
    position: absolute;
    left: 442px;
    top: 20px;
    width: 316px;
    height: 560px;
    background: var(--white);
    overflow: hidden;
    box-shadow: 0 6px 24px rgba(0, 0, 0, 0.12);
  }
  .hero {
    position: absolute;
    inset: 0 0 auto 0;
    height: 420px;
    background:
      linear-gradient(200deg, rgba(255,255,255,0.22) 0%, rgba(255,255,255,0) 45%),
      linear-gradient(135deg, var(--coral) 0%, var(--pink) 55%, var(--pink-light) 100%);
  }
  .hero-facet {
    position: absolute;
    inset: 0;
    width: 100%;
    height: 100%;
  }
  .stair-climber-mark {
    position: absolute;
    left: 50%;
    top: 120px;
    width: 78px;
    height: 86px;
    transform: translateX(-50%);
    border-radius: 10px;
    background: linear-gradient(160deg, rgba(255,255,255,0.9), rgba(255,255,255,0.7));
  }
  .wave-divider {
    position: absolute;
    left: 0;
    top: 370px;
    width: 316px;
    height: 80px;
  }
  .loading-spinner {
    position: absolute;
    left: 50%;
    top: 468px;
    width: 40px;
    height: 40px;
    transform: translateX(-50%);
  }
</style>
</head>
<body>
  <main class="canvas">
    <section class="splash-screen" aria-label="App splash screen">
      <div class="hero">
        <svg class="hero-facet" viewBox="0 0 316 420" preserveAspectRatio="none" aria-hidden="true">
          <polygon points="120,0 316,0 316,260" fill="var(--white)" opacity="0.12"/>
          <polygon points="0,180 0,420 220,420" fill="var(--coral)" opacity="0.18"/>
        </svg>
        <div class="stair-climber-mark" role="img" aria-label="White pictogram of a figure stepping up a staircase"></div>
      </div>

      <svg class="wave-divider" viewBox="0 0 316 80" preserveAspectRatio="none" aria-hidden="true">
        <path d="M0,28 C40,8 70,40 110,24 C150,8 180,36 220,22 C260,8 290,30 316,18 L316,80 L0,80 Z"
              fill="var(--pink-pale)" opacity="0.55"/>
        <path d="M0,40 C35,26 75,52 120,38 C165,24 200,48 245,34 C280,24 300,38 316,32 L316,80 L0,80 Z"
              fill="var(--white)" opacity="0.7"/>
        <path d="M0,52 C45,40 85,62 135,50 C185,38 225,60 270,48 C292,42 306,48 316,46 L316,80 L0,80 Z"
              fill="var(--white)"/>
      </svg>

      <svg class="loading-spinner" viewBox="0 0 40 40" role="img" aria-label="Loading">
        <g fill="var(--spinner)">
          <circle cx="20" cy="5" r="3" opacity="1"/>
          <circle cx="30.6" cy="9.4" r="3" opacity="0.9"/>
          <circle cx="35" cy="20" r="3" opacity="0.8"/>
          <circle cx="30.6" cy="30.6" r="3" opacity="0.7"/>
          <circle cx="20" cy="35" r="3" opacity="0.6"/>
          <circle cx="9.4" cy="30.6" r="3" opacity="0.5"/>
          <circle cx="5" cy="20" r="3" opacity="0.4"/>
          <circle cx="9.4" cy="9.4" r="3" opacity="0.3"/>
        </g>
      </svg>
    </section>
  </main>
</body>
</html>
```